Halvern Ditchworks LTD - website for irrigation & Landscape Lighting & Buried service wire

Looking for a website to help promote my business with Irrigation (installation, service, etc) and buried service wire/drainage solutions.

Commercial/Residential

Landscape lighting.

I’ll get photos in the trucks and trailers to upload as well maybe the machine as well.

Target Market(s)

Homeowners who want green grass and beautiful gardens. Beautiful landscape lighting

Industry/Entity Type

Irrigation systems and landscape lighting and buried service wire to homes and offering Drainage soltions.

Coding

Coded - Design and coding required

Number of Pages Required

4 page

Colors
F0912C
F2A743
F7CA91
FBE8D2
FDF5EE

Requirements
Must have
• was hoping to link up my email on halvernditchworks@mailbarn.net with the website if possible.
Nice to have
• Page for Irrigation, page for landscape lighting, page buried service wire & drainage soltions.

```html
<!DOCTYPE html>
<html lang="en">
<head>
<meta charset="utf-8">
<title>Halvern Ditchworks LTD — Irrigation, Landscape Lighting, Service Wire &amp; Drainage</title>
<link href="https://fonts.googleapis.com/css2?family=Montserrat:wght@400;500;600;700&display=swap" rel="stylesheet">
<style>
:root{
  --orange:#F0912C;
  --orange-2:#F2A743;
  --peach:#F7CA91;
  --cream:#FBE8D2;
  --ivory:#FDF5EE;
  --ink:#111111;
  --body:#555555;
  --white:#ffffff;
}
*{margin:0;padding:0;box-sizing:border-box}
html,body{width:1200px;height:2928px;overflow:hidden}
body{font-family:"Montserrat",sans-serif;color:var(--ink);background:var(--white);position:relative}
a{color:inherit;text-decoration:none}
.abs{position:absolute}

/* header */
.site-header{position:absolute;left:0;top:0;width:1200px;height:70px;background:var(--white)}
.brand{position:absolute;left:141px;top:19px;width:140px;font-size:13px;line-height:16px;font-weight:700;color:var(--orange);text-transform:uppercase;letter-spacing:.2px}
.main-nav{position:absolute;left:398px;top:28px;display:flex;gap:27px;font-size:11.5px;font-weight:500;letter-spacing:.5px;white-space:nowrap}
.main-nav .active{color:var(--orange);border-bottom:1px solid var(--orange);padding-bottom:4px}
.btn{display:inline-flex;align-items:center;justify-content:center;background:var(--orange);color:var(--white);border-radius:20px;font-size:12px;font-weight:600;letter-spacing:.8px;text-transform:uppercase}
.btn-contact{position:absolute;left:940px;top:18px;width:119px;height:35px}

/* hero */
.hero{position:absolute;left:0;top:70px;width:1200px;height:487px;
  background:linear-gradient(100deg,#1f3310 0%,#2f4a18 30%,#5a6e22 55%,#a7942f 78%,#e3b545 100%)}
.hero::after{content:"";position:absolute;inset:0;background:linear-gradient(90deg,rgba(0,0,0,.35) 0%,rgba(0,0,0,.1) 55%,rgba(0,0,0,0) 100%)}
.hero-content{position:absolute;left:141px;top:134px;width:500px;z-index:1;color:var(--white)}
.hero h1{font-size:31px;line-height:47px;font-weight:600;width:500px}
.hero-lead{margin-top:24px;border-left:2px solid var(--orange);padding-left:11px;font-size:12.5px;line-height:23px;width:475px}
.btn-quote{margin-top:28px;width:161px;height:35px}

/* services */
.blob{position:absolute;width:390px;height:380px}
.service-text{position:absolute;width:420px}
.service-text h2{font-size:25px;font-weight:600;line-height:32px;white-space:nowrap}
.service-text h2 span{color:var(--orange)}
.tagline{margin-top:26px;border-left:2px solid var(--orange);padding-left:11px;font-size:13px;font-weight:500;line-height:23px}
.service-text p.desc{margin-top:14px;font-size:13px;line-height:22.7px;color:var(--body)}
.btn-more{margin-top:26px;width:123px;height:35px}

/* testimonials */
.testimonials-title{position:absolute;left:0;top:2078px;width:1200px;text-align:center;font-size:25px;font-weight:600}
.testimonials-title span{color:var(--orange)}
.testimonials-sub{position:absolute;left:0;top:2129px;width:1200px;text-align:center;font-size:13px;font-weight:500}
.quote{position:absolute;left:141px;top:2259px;width:480px;font-size:13px;line-height:22.7px;color:#333}
.quote-name{position:absolute;left:141px;top:2388px;font-size:16px;font-weight:600;color:var(--orange)}
.slider-arrows{position:absolute;left:141px;top:2462px}
.avatar{position:absolute;border-radius:50%}

/* footer */
.site-footer{position:absolute;left:0;top:2614px;width:1200px;height:314px;
  background:linear-gradient(180deg,#2a2820 0%,#1d1c17 60%,#141310 100%);color:var(--white)}
.footer-brand{position:absolute;left:141px;top:78px;width:190px;font-size:24px;line-height:29px;font-weight:700;color:var(--white);text-transform:uppercase}
.footer-col{position:absolute;top:58px}
.footer-col h3{font-size:16px;font-weight:600;color:var(--orange);margin-bottom:12px}
.footer-col li{list-style:none;font-size:13px;line-height:27.5px;white-space:nowrap}
.contact-row{display:flex;gap:12px;font-size:13px;line-height:20px;margin-bottom:10px;align-items:flex-start}
.contact-row svg{flex:none;margin-top:2px}
.footer-rule{position:absolute;left:141px;top:258px;width:918px;height:1px;background:rgba(255,255,255,.3)}
.copyright{position:absolute;left:141px;top:279px;font-size:13px}
.social{position:absolute;left:926px;top:274px;display:flex;gap:13px}
.social span{width:24px;height:24px;border-radius:50%;background:var(--orange);display:block}
</style>
</head>
<body>

<header class="site-header">
  <div class="brand">Halvern Ditchworks LTD</div>
  <nav class="main-nav">
    <a class="active" href="#">HOME</a>
    <a href="#">IRRIGATION</a>
    <a href="#">LANDSCAPE LIGHTING</a>
    <a href="#">SERVICE WIRE &amp; DRAINAGE</a>
  </nav>
  <a class="btn btn-contact" href="#">Contact Us</a>
</header>

<section class="hero" role="img" aria-label="Sprinkler spraying water over a green field at golden sunset">
  <div class="hero-content">
    <h1>Transform Your Outdoor Space With Our Expert Irrigation And Lighting Solutions</h1>
    <p class="hero-lead">Get The Perfect Blend Of Form And Function With Our State-Of-The-Art Irrigation Systems And Landscape Lighting. Trust Our Experienced Team With Buried Service Wire And Drainage For Your Home.</p>
    <a class="btn btn-quote" href="#">Get A Free Quote</a>
  </div>
</section>

<svg width="0" height="0" style="position:absolute">
  <defs>
    <path id="blobShape" d="M175 8 C240 -2 330 80 368 150 C395 215 352 295 262 322 C180 350 75 372 32 352 C-4 328 0 250 40 152 C72 72 112 18 175 8Z"/>
    <linearGradient id="gSky" x1="0" y1="0" x2="0" y2="1"><stop offset="0" stop-color="#a9bfd8"/><stop offset=".6" stop-color="#c9c6b8"/><stop offset="1" stop-color="#6f7a55"/></linearGradient>
    <linearGradient id="gGarden" x1="0" y1="0" x2="0" y2="1"><stop offset="0" stop-color="#2f3b22"/><stop offset=".5" stop-color="#5f7a2e"/><stop offset="1" stop-color="#3d4a22"/></linearGradient>
    <linearGradient id="gDesk" x1="0" y1="0" x2="1" y2="1"><stop offset="0" stop-color="#d8d2c8"/><stop offset=".5" stop-color="#7a4a2a"/><stop offset="1" stop-color="#2a1c15"/></linearGradient>
    <linearGradient id="gPortrait" x1="0" y1="0" x2="0" y2="1"><stop offset="0" stop-color="#b9c3cd"/><stop offset=".5" stop-color="#6e7378"/><stop offset="1" stop-color="#23262c"/></linearGradient>
  </defs>
</svg>

<!-- Irrigation -->
<svg class="blob" style="left:150px;top:654px" viewBox="0 0 390 380" role="img" aria-label="Rotating agricultural sprinkler head spraying at dawn">
  <use href="#blobShape" transform="translate(12 4)" fill="none" stroke="var(--orange)" stroke-width="1.4"/>
  <use href="#blobShape" fill="url(#gSky)"/>
</svg>
<div class="service-text" style="left:639px;top:697px">
  <h2>Irrigation <span>Systems</span></h2>
  <p class="tagline">Efficient and Effective Watering Solutions for Your Lawn and Garden</p>
  <p class="desc">Our irrigation systems are designed to provide your lawn and garden with the right amount of water, without wasting a single drop. With our expert installation and service, you can rest assured that your plants will receive the nourishment they need to thrive.</p>
  <a class="btn btn-more" href="#">Learn More</a>
</div>

<!-- Landscape Lighting -->
<div class="service-text" style="left:141px;top:1174px;width:410px">
  <h2>Landscape <span>Lighting</span></h2>
  <p class="tagline">Enhance Your Outdoor Space with Beautiful and Functional Lighting Solutions</p>
  <p class="desc">Our landscape lighting solutions are designed to enhance the beauty and functionality of your outdoor space. From subtle pathway lighting to dramatic spotlights, we'll work with you to create a lighting plan that meets your needs and complements your landscape.</p>
  <a class="btn btn-more" href="#">Learn More</a>
</div>
<svg class="blob" style="left:665px;top:1131px" viewBox="0 0 390 380" role="img" aria-label="Garden at dusk lit by pathway bollard lights">
  <use href="#blobShape" transform="translate(12 4)" fill="none" stroke="var(--orange)" stroke-width="1.4"/>
  <use href="#blobShape" fill="url(#gGarden)"/>
</svg>

<!-- Service Wire & Drainage -->
<svg class="blob" style="left:150px;top:1609px" viewBox="0 0 390 380" role="img" aria-label="Crew laying buried service wire and drainage pipe in a fresh trench">
  <use href="#blobShape" transform="translate(12 4)" fill="none" stroke="var(--orange)" stroke-width="1.4"/>
  <use href="#blobShape" fill="url(#gDesk)"/>
</svg>
<div class="service-text" style="left:639px;top:1674px">
  <h2>Service Wire <span>&amp; Drainage</span></h2>
  <p class="tagline">Buried Service Wire and Drainage Solutions for Your Home</p>
  <p class="desc">Our team of experienced professionals will trench and bury your service wire with precision and care. We'll also design drainage that moves water away from your home, keeping your yard dry, your foundation safe and your lawn healthy all year.</p>
  <a class="btn btn-more" href="#">Learn More</a>
</div>

<!-- Testimonials -->
<h2 class="testimonials-title">What Our <span>Customers</span> Say</h2>
<p class="testimonials-sub">Hear from Our Satisfied Clients</p>
<p class="quote">They maintain around 52 acres for us including several thousand sq ft or beds. Always answer thr phone and very prompt if we ever have an issue. Great guys all the way around! It is a long established fact that a reader will be distracted by the readable content of a page when looking at its layout.</p>
<p class="quote-name">Marcus Delane</p>
<svg class="slider-arrows" width="130" height="20" viewBox="0 0 130 20" aria-label="Previous and next">
  <path d="M36 10H2M9 3L2 10L9 17" fill="none" stroke="#111" stroke-width="1.5"/>
  <path d="M92 10H127M120 3L127 10L120 17" fill="none" stroke="#111" stroke-width="1.5"/>
</svg>

<svg class="abs" style="left:708px;top:2186px" width="240" height="345" viewBox="0 0 240 345" role="img" aria-label="Portrait of a client in a dark blazer">
  <rect x="8" y="4" width="228" height="338" rx="114" fill="none" stroke="var(--orange)" stroke-width="1.4"/>
  <rect x="2" y="2" width="228" height="338" rx="114" fill="url(#gPortrait)"/>
</svg>
<div class="avatar" style="left:946px;top:2138px;width:111px;height:111px;background:linear-gradient(160deg,#6b5a4d,#3a2a24 60%,#8a1a26)" role="img" aria-label="Client portrait"></div>
<div class="avatar" style="left:592px;top:2408px;width:80px;height:80px;background:linear-gradient(160deg,#6f9bb0,#3c4a3a 60%,#2b2b2b)" role="img" aria-label="Client portrait"></div>
<div class="avatar" style="left:967px;top:2419px;width:69px;height:69px;background:linear-gradient(160deg,#5a5a5a,#3a302a 60%,#1f1f1f)" role="img" aria-label="Client portrait"></div>

<!-- Footer -->
<footer class="site-footer" role="img" aria-label="Dark garden backdrop behind footer content">
  <div class="footer-brand">Halvern Ditchworks LTD</div>

  <div class="footer-col" style="left:459px">
    <h3>Quick Links</h3>
    <ul><li>Home</li><li>Irrigation</li><li>Landscape Lighting</li><li>Service Wire &amp; Drainage</li></ul>
  </div>
  <div class="footer-col" style="left:671px">
    <h3>Useful Links</h3>
    <ul><li>Contact</li><li>Privacy Policy</li><li>Terms of Service</li></ul>
  </div>
  <div class="footer-col" style="left:839px;width:240px">
    <h3>Contact Info</h3>
    <div class="contact-row">
      <svg width="17" height="20" viewBox="0 0 17 20"><path d="M8.5 1C4.6 1 1.5 4 1.5 7.8 1.5 12.5 8.5 19 8.5 19S15.5 12.5 15.5 7.8C15.5 4 12.4 1 8.5 1Z" fill="none" stroke="var(--orange)" stroke-width="2"/><circle cx="8.5" cy="7.8" r="2.5" fill="var(--orange)"/></svg>
      <span>Address Line 1, Address Line 2, Address Line 3.</span>
    </div>
    <div class="contact-row">
      <svg width="17" height="14" viewBox="0 0 17 14"><rect x="0" y="1" width="17" height="12" rx="1.5" fill="var(--orange)"/><path d="M1 2.5L8.5 8L16 2.5" fill="none" stroke="#1d1c17" stroke-width="1.4"/></svg>
      <span>halvernditchworks@mailbarn.net</span>
    </div>
    <div class="contact-row">
      <svg width="16" height="16" viewBox="0 0 16 16"><path d="M3.2 1L6 1.4 7 4.6 5.2 6C6.2 8 7.9 9.7 10 10.8L11.4 9 14.6 10 15 12.8C15 14 14 15 12.8 15 6.3 15 1 9.7 1 3.2 1 2 2 1 3.2 1Z" fill="var(--orange)"/></svg>
      <span>123-456-7890</span>
    </div>
  </div>

  <div class="footer-rule"></div>
  <p class="copyright">© 2024 Halvern Ditchworks. All rights reserved.</p>
  <div class="social" aria-label="Social links"><span></span><span></span><span></span><span></span></div>
</footer>

</body>
</html>
```